Plum Stride Buisiness card

needing a Business card for our company - Plum Stride.
Plum stride is co owned by Nell and Dermot Wardrop (Husband and Wife)
Services Plum Stride provides include:
Dietetic/nutrition Consultations, weight loss coaching programs, personal and group training, post injury rehab, health and nutrition presentations and Health Retreats.
Nell:
Accredited Practicing Dietitian & Personal trainer
Dermot:
Personal trainer, rehab trainer & Strength and conditioning coach
At this stage the business cards will be made just for Nell.
She has a training studio in Armadale and Dietetics private practice in Richmond.
Mobile services are also available (i.e. meet at house or local cafe)

We need the card to look smart, modern and combine both nutrition and training.
We already have a logo which I will attach.
I was initial thinking i black background but am open to suggestions.

Target Market(s)

Health concious, People with money,

Industry/Entity Type

Nutrition

Contact Information for Business Card

Plum Stride
Nell Wardrop
M: 0431907265
E: plumstride@postwren.com
W: www.plumstride.com.au
Address:
Dietetics: Level 1, 88 Tolley Street
Kelsall VIC 3188
Training: Private Studio, behind 517 Merrow St
ARMADALE, VIC, 3143

Requirements
Must have
• Must have logo (see attached) please not the one we use is the top left (blue and green)
please note attachment is top left (green and blue)

needs to be clear to read - the font needs to be clear and sharp and the background cannot be too busy.eg funny patterns.
Could I please see a card with a line for 'appointment time/date:' possibly on the back. Would like to see what this looks like.
Nell Wardrop's Profile (side of card) must include "Accredited Practicing Dietitian" and "Personal Trainer."
I like when the services plum stride provide are in dot form.
Nice to have
• would like the card to be 2 sides
first side:
Plum stride logo - Large
services plum stride provides: Dietetic/nutrition Consultations, weight loss coaching programs, personal and group training, post injury rehab, health and nutrition presentations and Health Retreats.
web address
second side:
smaller logo
Details for Nell:
Accredited Practicing Dietitian
Personal Trainer
Contact Details:
M: 0431907265
E: plumstride@postwren.com
Address:
Kelsall VIC 3188
ARMADALE, VIC, 3143
Should not have
• Dietetic + nutrition consultations
Should say dietetic/nutrition consultations (first letter of words in capitals please)
Please write phone number as 0431 907 265
Not: 04 31 907265
- note numbers as 4, 3, 3.

```html
<!DOCTYPE html>
<html lang="en">
<head>
<meta charset="utf-8">
<title>Plum Stride – Business Card</title>
<link href="https://fonts.googleapis.com/css2?family=Arimo:ital,wght@0,400;0,700;1,400;1,700&display=swap" rel="stylesheet">
<style>
  :root{
    --backdrop:#e9ebee;
    --navy:#1d3f9e;
    --navy-deep:#122d82;
    --navy-light:#2a52b8;
    --green:#7cc243;
    --ink:#111111;
    --label:#1f4aa8;
    --muted:#8a8a8a;
    --white:#ffffff;
  }
  *{box-sizing:border-box;margin:0;padding:0}
  html,body{width:1200px;height:900px;overflow:hidden}
  body{
    background:var(--backdrop);
    font-family:"Arimo",Arial,sans-serif;
    position:relative;
  }
  .card{
    position:absolute;
    width:560px;height:320px;
    border-radius:4px;
    box-shadow:0 6px 18px rgba(0,0,0,.18);
    overflow:hidden;
  }
  /* ---------- back side ---------- */
  .card--services{
    left:40px;top:130px;
    background:linear-gradient(165deg,var(--navy-light) 0%,var(--navy) 45%,var(--navy-deep) 100%);
    color:var(--white);
  }
  .card--services .sweep{
    position:absolute;inset:0;width:100%;height:100%;
  }
  .service-list{
    position:absolute;left:34px;top:60px;
    list-style:none;font-size:15px;line-height:24px;
  }
  .service-list li{display:flex;align-items:center;gap:8px}
  .service-list li::before{
    content:"";width:7px;height:7px;border-radius:50%;
    background:#d9dde8;flex:none;
  }
  .brand-large{
    position:absolute;right:36px;top:72px;
    display:flex;align-items:center;gap:12px;
    font-size:30px;font-weight:700;color:var(--white);
  }
  .brand-large .dot{
    width:22px;height:22px;border-radius:50%;background:var(--green);
  }
  .web-address{
    position:absolute;right:44px;top:205px;
    font-size:15px;letter-spacing:.5px;
  }
  .appt-field{
    position:absolute;left:34px;right:34px;top:232px;height:54px;
  }
  .appt-field .line-box{
    position:absolute;left:150px;right:0;top:0;height:26px;
    background:var(--white);border-radius:5px;
  }
  .appt-field .tab{
    position:absolute;left:0;top:22px;width:150px;height:32px;
    background:var(--white);border-radius:5px 0 5px 5px;
    color:#333;font-size:14px;padding:8px 10px;
  }
  /* ---------- front side ---------- */
  .card--profile{
    left:600px;top:450px;
    background:var(--white);
    border:1px solid #d8d8d8;
  }
  .brand-small{
    position:absolute;left:34px;top:150px;
    display:flex;align-items:center;gap:10px;
    font-size:36px;font-weight:400;color:var(--navy);
    letter-spacing:-.5px;
  }
  .brand-small .dot{
    width:18px;height:18px;border-radius:50%;background:var(--green);
  }
  .tagline{
    position:absolute;left:52px;top:198px;
    font-size:11px;font-style:italic;color:var(--muted);
  }
  .profile{
    position:absolute;left:276px;top:42px;right:20px;
  }
  .profile .name{
    font-size:20px;font-weight:700;font-style:italic;color:var(--navy);
    margin-left:16px;
  }
  .profile .roles{
    margin-top:12px;font-size:13px;line-height:16px;color:var(--label);
  }
  .contact{
    margin-top:18px;
    display:grid;grid-template-columns:62px 1fr;
    font-size:13px;line-height:16px;
  }
  .contact dt{color:var(--label);font-style:italic}
  .contact dd{color:var(--ink);letter-spacing:.3px}
  .contact .gap{margin-top:10px}
</style>
</head>
<body>

  <section class="card card--services" aria-label="Card back: services">
    <svg class="sweep" viewBox="0 0 560 320" preserveAspectRatio="none" aria-hidden="true">
      <path d="M0 250 Q280 200 560 150 L560 320 L0 320 Z" fill="#163591" opacity=".55"/>
    </svg>
    <ul class="service-list">
      <li>Dietetic/Nutrition Consultations</li>
      <li>Weight loss coaching programs</li>
      <li>Personal and group training</li>
      <li>Post injury rehab</li>
      <li>Health and Nutrition presentations</li>
      <li>Health Retreats</li>
    </ul>
    <div class="brand-large"><span class="dot"></span>Plum Stride</div>
    <p class="web-address">www.plumstride.com.au</p>
    <div class="appt-field">
      <div class="line-box"></div>
      <div class="tab">Appt:</div>
    </div>
  </section>

  <section class="card card--profile" aria-label="Card front: contact details">
    <div class="brand-small"><span class="dot"></span>Plum Stride</div>
    <p class="tagline">"Every step counts!"</p>
    <div class="profile">
      <h1 class="name">Nell Wardrop</h1>
      <p class="roles">Accredited Practicing Dietitian<br>Personal Trainer</p>
      <dl class="contact">
        <dt>Mobile:</dt><dd>0431 907 265</dd>
        <dt>Email:</dt><dd>plumstride@postwren.com</dd>
        <dt>Website:</dt><dd>www.plumstride.com.au</dd>
        <dt class="gap">Dietetics:</dt><dd class="gap">Level 1, 88 Tolley Street<br>Kelsall VIC 3188</dd>
      </dl>
    </div>
  </section>

</body>
</html>
```